Business Card Design - Photographer

I am a landscape photographer and I require a business card design. 

I require two designs:
1)  a double sided business card
 and
b)  a single sided business card 

The single sided design can either be the same as the double sided (with just one side having all the information)....or it can be an entire new design. Its up to you.

My corporate colours are (CMYK):

Blue   69, 32, 0, 0
Grey  72,  64,  47,  31
Green  32,  2,  91,  0
Yellow   0, 19, 92, 0
Orange  0, 39, 75, 0

Colour space in final file should be in CMYK.

The details that need to be included on the card:

- Use the provided Logo
- Name: Lukas Wendrovski
- Email:   sales@vistaplume.com.au
- Website:    vistaplume.com.au
- Twitter:    twitter.com/vistaplume
- Facebook:   facebook.com/vistaplume
- Mobile  0415 309 662

Please use the attached template to design the logo to the specified size, including the marked bleed lines. I have also attached my logo in PNG (transparent background) and ai format for you to use.

The final file should be:
- Photoshop version with layers so I can edit the name/text etc. All non vector files should be high resolution at 1039 x 697 pixels at 300 dpi.

I also require a file as:
- Vector based PDF

Anyway questions please contact me.

Thank you

Industry/Entity Type

Landscape

Logo styles of interest
Pictorial/Combination Logo
Abstract Logo
Wordmark Logo
Lettermark Logo
Requirements
Must have
• The details that need to be included on the card:

- Use the provided Logo
- Name: Lukas Wendrovski
- Email: sales@vistaplume.com.au
- Website: vistaplume.com.au
- Twitter: twitter.com/vistaplume
- Facebook: facebook.com/vistaplume
- Mobile 0415 309 662

```html
<!DOCTYPE html>
<html lang="en">
<head>
<meta charset="utf-8">
<title>Vista Plume – Business Cards</title>
<link href="https://fonts.googleapis.com/css2?family=Cinzel:wght@600&family=Questrial&display=swap" rel="stylesheet">
<style>
  :root {
    --backdrop-light: #9fb0ad;
    --backdrop-mid: #8a9d9a;
    --backdrop-dark: #73878a;
    --card-light: #eceeec;
    --card-shade: #dcdfdc;
    --ink-navy: #2b3557;
    --ink-text: #3b4160;
    --label-ink: #111111;
  }
  * { margin: 0; padding: 0; box-sizing: border-box; }
  html, body { width: 1200px; height: 848px; overflow: hidden; }
  body { position: relative; font-family: "Questrial", sans-serif; }

  .backdrop {
    position: absolute; inset: 0;
    background:
      radial-gradient(ellipse at 30% 25%, var(--backdrop-light) 0%, transparent 60%),
      radial-gradient(ellipse at 80% 80%, var(--backdrop-dark) 0%, transparent 65%),
      var(--backdrop-mid);
  }

  .board-label {
    position: absolute;
    font-family: "Questrial", sans-serif;
    font-size: 46px;
    line-height: 1;
    color: var(--label-ink);
  }
  .board-label--front { left: 44px; top: 40px; }
  .board-label--back { left: 30px; top: 449px; }
  .board-label--single { left: 612px; top: 234px; }

  .card {
    position: absolute;
    background: radial-gradient(ellipse at 40% 40%, var(--card-light) 0%, var(--card-shade) 100%);
    color: var(--ink-text);
  }
  .card--front { left: 82px; top: 91px; width: 467px; height: 312px; }
  .card--back { left: 82px; top: 500px; width: 467px; height: 316px; }
  .card--single { left: 657px; top: 296px; width: 495px; height: 332px; }

  .brand-dot {
    position: absolute;
    border-radius: 50%;
    background: var(--ink-navy);
  }
  .brand-name {
    position: absolute;
    font-family: "Cinzel", serif;
    font-weight: 600;
    color: var(--ink-navy);
    white-space: nowrap;
    transform: translateX(-50%);
    line-height: 1;
  }

  /* Front */
  .card--front .brand-dot { width: 120px; height: 120px; left: 173px; top: 60px; }
  .card--front .brand-name { left: 233px; top: 226px; font-size: 30px; letter-spacing: 1px; }
  .card--front .rule {
    position: absolute; left: 0; right: 0; top: 256px;
    height: 2px; background: var(--ink-navy);
  }

  /* Back */
  .card--back .brand-dot { width: 58px; height: 58px; left: 310px; top: 22px; }
  .card--back .brand-name { left: 341px; top: 96px; font-size: 18px; }
  .card--back .brand-rule {
    position: absolute; left: 256px; width: 170px; top: 118px;
    height: 1px; background: var(--ink-navy);
  }
  .card--back .contact { position: absolute; left: 32px; top: 165px; }
  .card--back .contact__name { font-size: 19px; margin-bottom: 7px; }
  .card--back .contact__line { font-size: 15px; line-height: 19px; }
  .card--back .contact__social { margin-top: 5px; }
  .card--back .contact__social .contact__line { font-size: 13px; line-height: 13px; }

  /* Single sided */
  .card--single .brand-dot { width: 52px; height: 52px; left: 222px; top: 27px; }
  .card--single .brand-name { left: 248px; top: 88px; font-size: 15px; }
  .card--single .brand-rule {
    position: absolute; left: 176px; width: 144px; top: 106px;
    height: 1px; background: var(--ink-navy);
  }
  .card--single .contact {
    position: absolute; left: 0; right: 0; top: 126px; text-align: center;
  }
  .card--single .contact__name { font-size: 24px; margin-bottom: 14px; }
  .card--single .contact__line { font-size: 18px; line-height: 29px; }
  .card--single .contact__social { margin-top: 12px; }
  .card--single .contact__social .contact__line { font-size: 15px; line-height: 17px; }
</style>
</head>
<body>
  <div class="backdrop" role="img" aria-label="Weathered grey-green concrete backdrop"></div>

  <div class="board-label board-label--front">Front:</div>
  <div class="board-label board-label--back">Back:</div>
  <div class="board-label board-label--single">Single sided:</div>

  <section class="card card--front">
    <span class="brand-dot"></span>
    <div class="brand-name">VISTA PLUME</div>
    <div class="rule"></div>
  </section>

  <section class="card card--back">
    <span class="brand-dot"></span>
    <div class="brand-name">VISTA PLUME</div>
    <div class="brand-rule"></div>
    <div class="contact">
      <p class="contact__name">Lukas Wendrovski</p>
      <p class="contact__line">web: vistaplume.com.au</p>
      <p class="contact__line">mail: sales@vistaplume.com.au</p>
      <p class="contact__line">tel: 0415 309 662</p>
      <div class="contact__social">
        <p class="contact__line">twitter.com/vistaplume</p>
        <p class="contact__line">facebook.com/vistaplume</p>
      </div>
    </div>
  </section>

  <section class="card card--single">
    <span class="brand-dot"></span>
    <div class="brand-name">VISTA PLUME</div>
    <div class="brand-rule"></div>
    <div class="contact">
      <p class="contact__name">Lukas Wendrovski</p>
      <p class="contact__line">mail: sales@vistaplume.com.au</p>
      <p class="contact__line">web: vistaplume.com.au</p>
      <p class="contact__line">tel: 0415 309 662</p>
      <div class="contact__social">
        <p class="contact__line">twitter.com/vistaplume</p>
        <p class="contact__line">facebook.com/vistaplume</p>
      </div>
    </div>
  </section>
</body>
</html>
```